Riverbend Trusted Home Care-Flyer for Patients

Our Home Health Care Agency, Riverbend Trusted Home Care, is seeking a flyer to advertise our services. We would like our flyer to convey professionalism, classiness and sophistication. We want our agency to come across as one that is well-established and recognized as being first-rate within the field.

We also want to appear original; we want to stand out.

Our theme colors, blue and green, from our logo should be incorporated into the flyer's design (refer below).

The top of the page should say (in a clear, bold font)-Seeking Care for your Loved One?

Our Logo, followed by our slogan, "Lean On Those Nearby", should be in the center. (This should make it appear as if our agency is the obvious solution to the consumer's quest in finding suitable care for their family member). This should be in a big font.
Below that, our agency's services should be listed in a very noticeable font...yet smaller than what's written above that.
The text should read:
Our Services Include:
*Experienced Certified Home Health Aides/ Live In Home Health Aides/Companions
*Nursing Services
*Alzheimer’s and Dementia Care
*Respite Care
*Postoperative Care
*Post Rehabilitation Care
*Running Errands
*Light Housekeeping
*Assistance with Bathing, Feeding and Grooming
*Meal Preparation
*Laundry and Linen Washing
*Mail and Bill Organization
*Medication Management
*Accompanying to Doctor’s Appointments
*And much more!
Below that, in a smaller, yet noticeable font:
As seasoned professionals, we know how to help our clients navigate and fulfill their various health care needs. Those nearby are here to help you get the attention that you merit.
Call Riverbend Trusted Home Care today to learn more about our first-rate services!
Below that, in a larger font, our phone number, website, our e-mail address.
*Out contact information will be provided to the project’s winner*.

*Pictures of Caregivers helping elderly patient should be included in the advertisement as well. *

We provided advertisements of other Home Health Care Agencies attached below to use as a reference. Once again, while we are aiming for a similar idea; however, our goal is to stand out as the community's premiere home health care agency, the one that they want to choose. We want to be original as well!

Size: Standard Computer Paper Size. 8.5” x 11”.

Feel free to utilize your creative, designer flair!
We look forward to seeing the results!
Good luck!

Industry/Entity Type

Home Health Care

Font styles to use
Sans Serif

Requirements
Must have
• Refer above.
Nice to have
• Refer to attachment below to see how other home health care agencies advertise. While we are aiming for a similar idea, we would like to incorporate our logo, slogan and colors to make this flyer more unique and stand out. We would like to appear original.

```html
<!DOCTYPE html>
<html lang="en">
<head>
<meta charset="utf-8">
<title>Riverbend Trusted Home Care – Flyer</title>
<link href="https://fonts.googleapis.com/css2?family=Montserrat:wght@700;800&family=Roboto:wght@300;400;700&display=swap" rel="stylesheet">
<style>
  :root{
    --blue-deep:#0c4a8f;
    --blue-mid:#1a5aa3;
    --ink-blue:#17508f;
    --green:#8dc63f;
    --green-soft:#c9e39a;
    --green-pale:#eef6df;
    --panel:#f3f8e9;
    --white:#ffffff;
  }
  *{margin:0;padding:0;box-sizing:border-box}
  html,body{width:927px;height:1200px;overflow:hidden}
  body{font-family:"Roboto",Arial,sans-serif;color:var(--ink-blue)}
  .flyer{position:relative;width:927px;height:1200px;overflow:hidden;
    background:radial-gradient(ellipse 70% 60% at 50% 55%,var(--green-pale) 0%,#dcedbf 55%,var(--green-soft) 85%,#b4d871 100%)}
  .panel{position:absolute;left:44px;top:400px;width:838px;height:661px;background:var(--panel);border-radius:28px}
  .top-band{position:absolute;left:0;top:0;width:927px;height:720px}
  .headline{position:absolute;top:46px;left:0;width:927px;text-align:center;color:var(--white);
    font-family:"Montserrat",Arial,sans-serif;font-weight:800;font-size:55px;line-height:66px;letter-spacing:0.5px}
  .photo-shadow{position:absolute;left:130px;top:590px;width:680px;height:40px;border-radius:50%;
    background:radial-gradient(ellipse at center,rgba(60,80,40,.25),rgba(60,80,40,0) 70%)}
  .photo-frame{position:absolute;left:95px;top:188px;width:750px;height:409px;background:var(--white);border-radius:16px;padding:10px}
  .photo{width:100%;height:100%;border-radius:10px;
    background:linear-gradient(100deg,#dfe7dc 0%,#f1e6e2 30%,#e9f0f6 55%,#7fb0dc 72%,#e3ece2 100%)}
  .brand{position:absolute;top:625px;left:0;width:927px;text-align:center}
  .brand-dot{display:block;margin:0 auto 10px;width:58px;height:58px;border-radius:50%;background:var(--blue-deep)}
  .brand-name{font-family:"Montserrat",Arial,sans-serif;font-weight:700;font-size:19px;color:var(--ink-blue);letter-spacing:.3px}
  .slogan{position:absolute;top:751px;left:0;width:927px;text-align:center;
    font-family:"Montserrat",Arial,sans-serif;font-weight:700;font-size:28px;color:var(--ink-blue);letter-spacing:.4px}
  .services-head{position:absolute;top:803px;left:101px;width:724px;display:flex;align-items:center;gap:18px}
  .services-head .rule{flex:1;height:1px;background:var(--ink-blue);opacity:.6}
  .services-head h2{font-family:"Roboto",Arial,sans-serif;font-weight:700;font-size:16px;letter-spacing:.2px}
  .services{position:absolute;top:831px;left:100px;width:740px;display:flex}
  .services ul{list-style:none;font-weight:300;font-size:14.5px;line-height:19.6px}
  .services li{padding-left:7px;text-indent:-7px}
  .services li::before{content:"•"}
  .col-1{width:236px}
  .col-2{width:251px;padding-left:14px;border-left:1px solid var(--ink-blue);margin-top:6px;padding-top:0;height:110px}
  .col-3{padding-left:14px;border-left:1px solid var(--ink-blue);margin-top:6px;height:110px}
  .col-2 li:first-child,.col-3 li:first-child{margin-top:-6px}
  .about{position:absolute;top:987px;left:0;width:927px;text-align:center;font-weight:300;font-size:14.4px;line-height:19.5px}
  .about strong{font-weight:700}
  .contact{position:absolute;top:1087px;left:0;width:927px;text-align:center}
  .phone{font-family:"Montserrat",Arial,sans-serif;font-weight:700;font-size:32px;color:var(--ink-blue);letter-spacing:.5px}
  .contact p{font-weight:400;font-size:15.5px;line-height:25px}
</style>
</head>
<body>
<main class="flyer">
  <div class="panel"></div>

  <svg class="top-band" viewBox="0 0 927 720" aria-hidden="true">
    <defs>
      <linearGradient id="bandFill" x1="0" y1="0" x2="0" y2="1">
        <stop offset="0" stop-color="#0b4a8e"/>
        <stop offset="1" stop-color="#1a4f98"/>
      </linearGradient>
    </defs>
    <path d="M0 0H927V382Q463 700 0 366Z" fill="url(#bandFill)"/>
    <path d="M927 382Q463 700 0 366" fill="none" stroke="#ffffff" stroke-width="5"/>
  </svg>

  <h1 class="headline">SEEKING CARE FOR<br>YOUR LOVED ONE?</h1>

  <div class="photo-shadow"></div>
  <div class="photo-frame">
    <div class="photo" role="img" aria-label="Photo of a smiling caregiver in blue scrubs with a stethoscope sitting beside a happy elderly woman holding a cane"></div>
  </div>

  <div class="brand">
    <span class="brand-dot"></span>
    <span class="brand-name">RIVERBEND TRUSTED HOME CARE</span>
  </div>

  <h2 class="slogan">LEAN ON THOSE NEARBY</h2>

  <div class="services-head">
    <span class="rule"></span>
    <h2>OUR SERVICES INCLUDE:</h2>
    <span class="rule"></span>
  </div>

  <div class="services">
    <ul class="col-1">
      <li>Experienced Certified Home Health Aides/ Live In Home Health Aides/Companions</li>
      <li>Nursing Services</li>
      <li>Alzheimer’s and Dementia Care</li>
      <li>Respite Care</li>
    </ul>
    <ul class="col-2">
      <li>Postoperative Care</li>
      <li>Post Rehabilitation Care</li>
      <li>Running Errands</li>
      <li>Light Housekeeping</li>
      <li>Assistance with Bathing, Feeding and Grooming</li>
    </ul>
    <ul class="col-3">
      <li>Meal Preparation</li>
      <li>Laundry and Linen Washing</li>
      <li>Mail and Bill Organization</li>
      <li>Medication Management</li>
      <li>Accompanying to Doctor’s Appointments.</li>
    </ul>
  </div>

  <p class="about">
    As seasoned professionals, we know how to help our clients navigate and fulfill their various health care needs.<br>
    Those nearby are here to help you get the attention that you merit.<br>
    Call <strong>Riverbend Trusted Home Care</strong> today to learn more about our first-rate services!
  </p>

  <div class="contact">
    <div class="phone">CALL US (555) 318-4420</div>
    <p>www.riverbendtrustedcare.com</p>
    <p>hello@rbthc.com</p>
  </div>
</main>
</body>
</html>
```